Upmarket cover for top management book, ideally unlike most common cover pages

This book is about both good management and mismanagement and introduces novel concepts such as the inverse exponential law in strategy, No doubt that these concepts will be criticized by some management scholars. However, students, a few other colleagues and key top managers find the new ideas useful and eye-opening.
The cover must help communicate a deeper vision of management as an expression of life creation and a sort of "divine" energy.

Practical details:
Print and ebook cover page plus elements of the cover for each of the three main book sections.
Title; The Orchard
Subtitle: Harvest methods and the spiral rising rule
Author: Teodor B. Malvezzi
Publisher: Quillstone Author Press
Width x height: 13,97 x 21,59 cm (without bleed)
Spine: 14-15 cm according to paper color

Target Market(s)

Mostly managers who did not have the opportunity of attending postgraduate management studies such as the MBA

Industry/Entity Type

Mostly high technology

Font styles to use
Serif
Sans Serif
Other font styles liked:
• Arial nova, Arial light

Requirements
Must have
• Preferably cover and back cover on white background, but any good proposals would do.
Nice to have
• An image of bright and reassuring, albeit potentially unlimited, strength. Ideally the cover design should show that good management is good for the COMMON GOOD of society
Should not have
• Please do not show images of people and no proposals reminiscent of other management and strategy book covers

```html
<!DOCTYPE html>
<html lang="en">
<head>
<meta charset="UTF-8">
<title>The Orchard — Book Cover</title>
<link rel="stylesheet" href="https://fonts.googleapis.com/css2?family=Playfair+Display:wght@400;500&family=Cormorant+SC:wght@500;600&family=Cinzel:wght@500&display=swap">
<style>
  :root {
    --backdrop: #353535;
    --paper: #ffffff;
    --paper-shade: #f1f1f1;
    --gold-light: #e9c77a;
    --gold: #c9973f;
    --gold-deep: #a5752a;
    --ink: #2e2e2e;
  }
  * { margin: 0; padding: 0; box-sizing: border-box; }
  html, body {
    width: 1200px;
    height: 1200px;
    overflow: hidden;
    background: var(--backdrop);
  }
  .canvas {
    width: 1200px;
    height: 1200px;
    display: flex;
    align-items: center;
    justify-content: center;
  }
  .cover {
    position: relative;
    width: 712px;
    height: 1100px;
    background: linear-gradient(200deg, var(--paper) 40%, var(--paper-shade) 100%);
    text-align: center;
  }
  .gold-text {
    background: linear-gradient(100deg, var(--gold-deep) 0%, var(--gold) 35%, var(--gold-light) 60%, var(--gold) 100%);
    -webkit-background-clip: text;
    background-clip: text;
    color: transparent;
  }
  .title {
    position: absolute;
    top: 118px;
    left: 0;
    right: 0;
    font-family: "Playfair Display", serif;
    font-weight: 400;
    line-height: 1;
  }
  .title-article {
    display: block;
    font-size: 78px;
    letter-spacing: 1px;
  }
  .title-main {
    display: block;
    margin-top: 4px;
    font-size: 158px;
    letter-spacing: -2px;
  }
  .subtitle {
    position: absolute;
    top: 408px;
    left: 0;
    right: 0;
    font-family: "Cormorant SC", serif;
    font-weight: 600;
    font-size: 31px;
    line-height: 1.3;
    letter-spacing: 0.5px;
    color: var(--ink);
  }
  .emblem {
    position: absolute;
    top: 560px;
    left: 246px;
    width: 240px;
    height: 260px;
    border-radius: 8px;
    background: radial-gradient(ellipse at 55% 50%, var(--gold-light) 0%, var(--gold) 45%, rgba(201, 151, 63, 0.25) 75%, rgba(255, 255, 255, 0) 100%);
  }
  .author {
    position: absolute;
    bottom: 78px;
    left: 0;
    right: 0;
    font-family: "Cinzel", serif;
    font-weight: 500;
    font-size: 40px;
    letter-spacing: 4px;
  }
</style>
</head>
<body>
  <main class="canvas">
    <section class="cover">
      <h1 class="title gold-text">
        <span class="title-article">The</span>
        <span class="title-main">Orchard</span>
      </h1>
      <p class="subtitle">Harvest methods and the<br>Spiral rising rule</p>
      <div class="emblem" role="img" aria-label="Ornate golden key lying diagonally on the white cover"></div>
      <p class="author gold-text">Teodor B. Malvezzi</p>
    </section>
  </main>
</body>
</html>
```